Supplement Bottle Packaging and Design

We want to rebrand our current health supplements (see below). We do want it to be modern, vibrant and appealing supplement bottles. Very upscale and elegant as it targets primarily women.
NOTE: READ THE ATTACHED WORD DOCUMENT!
Bottle size: We are totally open to the bottle size and shape, as long it's a typical supplement bottle size to handle 90-120 capsules; what we mostly need is new bottle design/packaging. YOU DON’T HAVE TO USE THE CURRENT WHITE BOTTLE SHAPE, BUT ANYTHING MORE MODERN WOULD WORK!
Updates
We need more modern, clean sleek designs to choose from
Look and feel
Each slider illustrates characteristics of the customer's brand and the style your logo design should communicate.

```html
<!DOCTYPE html>
<html lang="en">
<head>
<meta charset="utf-8">
<title>Health Supplements – Bottle Range</title>
<link rel="stylesheet" href="https://fonts.googleapis.com/css2?family=Open+Sans:wght@700;800&display=swap">
<style>
  :root {
    --page-bg: #ffffff;
    --label-text: #ffffff;
    --cap: #2a2a2c;
    --cap-rim: #111112;
    --liver-top: #514882;
    --liver-bottom: #2a2b3d;
    --tummy-top: #a83c22;
    --tummy-bottom: #4a2422;
    --hormone-top: #2c9c48;
    --hormone-bottom: #2d4527;
    --sugar-top: #2f3596;
    --sugar-bottom: #252a4c;
  }
  html, body {
    margin: 0;
    padding: 0;
    width: 1200px;
    height: 825px;
    overflow: hidden;
    background: var(--page-bg);
  }
  .range { display: block; width: 1200px; height: 825px; }
  .product-name {
    font-family: "Open Sans", Verdana, sans-serif;
    font-weight: 800;
    fill: var(--label-text);
  }
  .product-name--liver { font-size: 49px; }
  .product-name--tummy { font-size: 46px; }
  .product-name--hormone { font-size: 39px; }
  .product-name--sugar { font-size: 32px; }
  .product-line {
    font-family: "Open Sans", Verdana, sans-serif;
    font-weight: 700;
    font-size: 12px;
    letter-spacing: 1.5px;
    fill: var(--label-text);
  }
  .capsule-count {
    font-family: "Open Sans", Verdana, sans-serif;
    font-weight: 700;
    font-size: 13.5px;
    fill: var(--label-text);
  }
  .cap-body { fill: var(--cap); }
  .cap-rim { fill: var(--cap-rim); }
  .label-sheen { fill: #ffffff; opacity: 0.07; }
</style>
</head>
<body>
<svg class="range" viewBox="0 0 1200 825" xmlns="http://www.w3.org/2000/svg">
  <defs>
    <linearGradient id="liver-fill" x1="0" y1="0" x2="0" y2="1">
      <stop offset="0" stop-color="var(--liver-top)"/>
      <stop offset="1" stop-color="var(--liver-bottom)"/>
    </linearGradient>
    <linearGradient id="tummy-fill" x1="0" y1="0" x2="0" y2="1">
      <stop offset="0" stop-color="var(--tummy-top)"/>
      <stop offset="1" stop-color="var(--tummy-bottom)"/>
    </linearGradient>
    <linearGradient id="hormone-fill" x1="0" y1="0" x2="0" y2="1">
      <stop offset="0" stop-color="var(--hormone-top)"/>
      <stop offset="1" stop-color="var(--hormone-bottom)"/>
    </linearGradient>
    <linearGradient id="sugar-fill" x1="0" y1="0" x2="0" y2="1">
      <stop offset="0" stop-color="var(--sugar-top)"/>
      <stop offset="1" stop-color="var(--sugar-bottom)"/>
    </linearGradient>
    <path id="bottle-shape" d="M -46,0 C -66,28 -80,46 -80,66 L -80,372 Q -80,414 -38,414 L 38,414 Q 80,414 80,372 L 80,66 C 80,46 66,28 46,0 Z"/>
    <path id="sheen-shape" d="M 10,0 C 60,60 80,160 60,414 L 80,414 L 80,66 C 80,46 66,28 46,0 Z"/>
    <g id="bottle-cap">
      <rect class="cap-body" x="-49" y="-64" width="98" height="56" rx="6"/>
      <rect class="cap-rim" x="-50" y="-12" width="100" height="14" rx="6"/>
    </g>
  </defs>

  <g class="bottle bottle--liver" transform="translate(248,250)">
    <use href="#bottle-cap"/>
    <use href="#bottle-shape" fill="url(#liver-fill)"/>
    <use href="#sheen-shape" class="label-sheen"/>
    <text class="product-name product-name--liver" transform="translate(16,355) rotate(-90)" textLength="310" lengthAdjust="spacingAndGlyphs">LIVER VIVRA</text>
    <text class="product-line" transform="translate(33,210) rotate(-90)" textLength="162" lengthAdjust="spacingAndGlyphs">HEALTH SUPPLEMENTS</text>
    <text class="capsule-count" x="4" y="390" text-anchor="middle">120 CAPSULES</text>
  </g>

  <g class="bottle bottle--tummy" transform="translate(475,250)">
    <use href="#bottle-cap"/>
    <use href="#bottle-shape" fill="url(#tummy-fill)"/>
    <use href="#sheen-shape" class="label-sheen"/>
    <text class="product-name product-name--tummy" transform="translate(10,359) rotate(-90)" textLength="316" lengthAdjust="spacingAndGlyphs">TUMMY VIVRA</text>
    <text class="product-line" transform="translate(25,210) rotate(-90)" textLength="162" lengthAdjust="spacingAndGlyphs">HEALTH SUPPLEMENTS</text>
    <text class="capsule-count" x="3" y="390" text-anchor="middle">120 CAPSULES</text>
  </g>

  <g class="bottle bottle--hormone" transform="translate(701,250)">
    <use href="#bottle-cap"/>
    <use href="#bottle-shape" fill="url(#hormone-fill)"/>
    <use href="#sheen-shape" class="label-sheen"/>
    <text class="product-name product-name--hormone" transform="translate(6,357) rotate(-90)" textLength="312" lengthAdjust="spacingAndGlyphs">HORMONE VIVRA</text>
    <text class="product-line" transform="translate(22,210) rotate(-90)" textLength="162" lengthAdjust="spacingAndGlyphs">HEALTH SUPPLEMENTS</text>
    <text class="capsule-count" x="4" y="390" text-anchor="middle">120 CAPSULES</text>
  </g>

  <g class="bottle bottle--sugar" transform="translate(912,250)">
    <use href="#bottle-cap"/>
    <use href="#bottle-shape" fill="url(#sugar-fill)"/>
    <use href="#sheen-shape" class="label-sheen"/>
    <text class="product-name product-name--sugar" transform="translate(9,358) rotate(-90)" textLength="313" lengthAdjust="spacingAndGlyphs">BLOOD SUGAR VIVRA</text>
    <text class="product-line" transform="translate(24,211) rotate(-90)" textLength="163" lengthAdjust="spacingAndGlyphs">HEALTH SUPPLEMENTS</text>
    <text class="capsule-count" x="6" y="390" text-anchor="middle">120 CAPSULES</text>
  </g>
</svg>
</body>
</html>
```